Mosvane Design

Looking for Mosvane banner and square design:
Mosvane Banner
W:1600 px H:400 px
Square
120x120

Logo attached.

Description: Data-Driven stock market portfolio management using quantitative analysis.

```html
<!DOCTYPE html>
<html lang="en">
<head>
<meta charset="UTF-8">
<title>Mosvane Banner</title>
<link href="https://fonts.googleapis.com/css2?family=Outfit:wght@500;600;700&display=swap" rel="stylesheet">
<style>
  :root {
    --canvas: #ffffff;
    --navy: #1a4f96;
    --sky: #1475bf;
    --ink: #0c0c0c;
    --brand: #133f78;
    --logo-blue: #1f5aa6;
    --panel-edge: #dbe6f2;
    --panel-a: #f2f7fd;
    --panel-b: #cfe0f3;
  }
  * { margin: 0; padding: 0; box-sizing: border-box; }
  html, body { width: 1200px; height: 300px; overflow: hidden; background: var(--canvas); }
  .banner {
    position: relative;
    width: 1200px;
    height: 300px;
    overflow: hidden;
    background: var(--canvas);
    font-family: "Outfit", sans-serif;
  }
  .banner__shapes { position: absolute; inset: 0; }
  .banner__illustration {
    position: absolute;
    left: 45px;
    top: 51px;
    width: 394px;
    height: 198px;
    border: 1px solid var(--panel-edge);
    border-radius: 2px;
    background: radial-gradient(ellipse at 55% 50%, var(--panel-b) 0%, var(--panel-a) 65%, #ffffff 100%);
  }
  .banner__headline {
    position: absolute;
    left: 440px;
    top: 0;
    width: 666px;
    height: 200px;
    color: var(--ink);
    font-weight: 500;
  }
  .headline__line {
    position: absolute;
    left: 0;
    width: 100%;
    text-align: center;
    white-space: nowrap;
    line-height: 1;
  }
  .headline__line--top {
    top: 46px;
    font-size: 36px;
    letter-spacing: 0.3px;
  }
  .headline__line--accent {
    top: 90px;
    font-size: 49px;
    font-weight: 700;
    color: var(--brand);
    letter-spacing: 0.2px;
  }
  .headline__line--bottom {
    top: 154px;
    font-size: 36px;
    letter-spacing: 0.4px;
  }
  .brand {
    position: absolute;
    left: 640px;
    top: 222px;
    display: flex;
    align-items: center;
    gap: 16px;
  }
  .brand__dot {
    width: 46px;
    height: 46px;
    border-radius: 50%;
    background: var(--logo-blue);
  }
  .brand__name {
    font-weight: 600;
    font-size: 34px;
    line-height: 1;
    color: var(--logo-blue);
    letter-spacing: 1px;
  }
</style>
</head>
<body>
  <div class="banner">
    <svg class="banner__shapes" width="1200" height="300" viewBox="0 0 1200 300" aria-hidden="true">
      <path d="M0 136 C 170 118, 330 170, 492 300 L 0 300 Z" fill="var(--navy)"/>
      <path d="M1012 0 C 1080 40, 1140 70, 1200 110 L 1200 0 Z" fill="var(--sky)"/>
    </svg>

    <div class="banner__illustration" role="img" aria-label="Isometric illustration of an analytics dashboard with charts, data blocks and people working around it"></div>

    <h1 class="banner__headline">
      <span class="headline__line headline__line--top">DATA-DRIVEN STOCK MARKET</span>
      <span class="headline__line headline__line--accent">PORTFOLIO MANAGEMENT</span>
      <span class="headline__line headline__line--bottom">USING QUANTITATIVE ANALYSIS.</span>
    </h1>

    <div class="brand">
      <span class="brand__dot"></span>
      <span class="brand__name">MOSVANE</span>
    </div>
  </div>
</body>
</html>
```